Safety Shoes Packaging - Box Design

We need a design for the box of safety shoes.
Our company is active in the industrial and construction sector.
Our brand logo is attached.
Also attached is the hang tag of the working gloves line for some consistency between the brand's product range.
They are intended for use in a wide variety of Industrial environments, like construction, cleaning and maintenance.
The final design should communicate
Safety
heavy duty use & toughness
durability
but also comfort and premium feel.
Packaging should also include a label with the following info - space:
Size:
Model:
Barcode
EN ISO 20345 S3 SRC
CE Symbol
Example of the label is also attached
Target Market(s)
Tradesmen, age 25-50
Industry/Entity Type
Construction, Landscape, Agriculture

```html
<!DOCTYPE html>
<html lang="en">
<head>
<meta charset="utf-8">
<title>VANTERRA Safety Shoes – Box Dieline</title>
<link rel="stylesheet" href="https://fonts.googleapis.com/css2?family=Montserrat:ital,wght@0,600;0,700;0,800;1,700&family=Black+Ops+One&family=Roboto:wght@400;700;900&display=swap">
<style>
  :root{
    --canvas:#ffffff;
    --flap:#3b424b;
    --panel-dark:#151617;
    --panel-mid:#2a2d31;
    --orange:#e8561f;
    --stripe-orange:#c8602f;
    --stripe-dark:#161616;
    --white:#ffffff;
    --ghost-name:#6b5d55;
    --cut:#8a2a5a;
    --icon-bg:#e7e7e7;
    --ink:#111111;
  }
  *{box-sizing:border-box;margin:0;padding:0}
  html,body{width:1200px;height:2233px;overflow:hidden;background:var(--canvas)}
  .canvas{position:relative;width:1200px;height:2233px;background:var(--canvas)}
  .dieline{position:absolute;left:16px;top:350px;width:1217px;height:1598px;transform:scale(0.96);transform-origin:0 0}
  .part{position:absolute;overflow:hidden}
  .flap{background:var(--flap)}
  .panel{background:
      radial-gradient(ellipse 70% 45% at 55% 75%, rgba(120,120,120,.28), transparent 70%),
      linear-gradient(180deg,var(--panel-dark),var(--panel-mid) 55%,var(--panel-dark));
      outline:1px solid var(--cut)}
  .hazard-band{position:absolute;background:repeating-linear-gradient(-60deg,var(--stripe-orange) 0 16px,var(--stripe-dark) 16px 32px)}
  .hazard-band.vertical{background:repeating-linear-gradient(-30deg,var(--stripe-orange) 0 16px,var(--stripe-dark) 16px 32px)}

  .brand-name{font-family:"Montserrat",sans-serif;font-weight:700;color:var(--orange);letter-spacing:2px;line-height:1;white-space:nowrap}

  /* side panels */
  .side-panel{left:255px;width:710px;height:255px}
  .side-panel.front{top:0}
  .side-panel.back{top:760px}
  .side-content{position:absolute;inset:0}
  .side-panel.back .side-content{transform:rotate(180deg)}
  .side-content .hazard-band{left:0;right:0;bottom:0;height:37px}
  .brand-block{position:absolute;left:38px;top:170px}
  .side-content .brand-name{font-size:38px}
  .use-icons{position:absolute;left:462px;top:65px;display:flex;gap:14px}
  .use-icon{width:56px;height:56px;border-radius:9px;background:var(--icon-bg)}
  .made-in{position:absolute;right:30px;top:184px;font-family:"Montserrat",sans-serif;font-style:italic;font-weight:700;font-size:14px;color:var(--white);letter-spacing:1px;white-space:nowrap}
  .made-in .brand-inline{font-style:normal;font-size:22px;letter-spacing:1.5px}

  /* flaps */
  .flap.tl{left:0;top:0;width:255px;height:255px}
  .flap.tr{left:965px;top:0;width:252px;height:255px}
  .flap.bl{left:0;top:760px;width:255px;height:255px}
  .flap.br{left:965px;top:760px;width:252px;height:255px}
  .flap.lid-l{left:178px;top:1015px;width:77px;height:505px;outline:1px solid var(--cut)}
  .flap.lid-r{left:965px;top:1015px;width:75px;height:505px;outline:1px solid var(--cut)}
  .flap.lid-b{left:255px;top:1520px;width:710px;height:78px;outline:1px solid var(--cut)}

  /* base */
  .base{left:255px;top:255px;width:710px;height:505px;background:var(--flap);outline:1px solid var(--cut)}
  .ghost-brand{position:absolute;left:0;right:0;top:300px;text-align:center}
  .ghost-brand .brand-name{color:var(--ghost-name);font-size:76px;letter-spacing:4px}

  /* end panels */
  .end-panel{top:255px;height:505px}
  .end-panel.label-end{left:0;width:255px}
  .end-panel.logo-end{left:965px;width:252px}
  .label-end .hazard-band{left:218px;top:0;width:37px;height:505px}
  .logo-end .hazard-band{left:0;top:0;width:35px;height:505px}
  .end-brand{position:absolute;left:150px;top:252px;width:320px;transform:translate(-50%,-50%) rotate(90deg);text-align:center}
  .end-brand .brand-name{font-size:44px}

  /* product label */
  .product-label{position:absolute;left:134px;top:252px;width:435px;height:192px;transform:translate(-50%,-50%) rotate(-90deg);background:var(--white);border-radius:16px;font-family:"Roboto",sans-serif;color:var(--ink)}
  .label-col{position:absolute;top:14px;bottom:14px}
  .col-barcode{left:14px;width:112px}
  .barcode-box{position:absolute;left:0;right:0;top:24px;bottom:8px;border:1px solid var(--ink);display:flex;align-items:center;justify-content:center;font-weight:700;font-size:13px}
  .col-size{left:140px;width:130px;border-left:1px solid var(--ink)}
  .shoe-art{position:absolute;left:14px;top:6px;width:80px;height:66px;background:linear-gradient(135deg,#e4e4e4,#bdbdbd);border-radius:6px}
  .size-line{position:absolute;left:14px;bottom:4px;display:flex;align-items:flex-end;gap:8px}
  .size-key{font-weight:700;font-size:14px;border-bottom:1px solid var(--ink);padding-bottom:2px}
  .size-value{font-weight:900;font-size:50px;line-height:.9}
  .col-model{left:280px;width:100px;border-left:1px solid var(--ink)}
  .model-key{position:absolute;left:12px;top:8px;font-weight:700;font-size:14px;border-bottom:1px solid var(--ink);padding-bottom:2px;width:70px}
  .norm{position:absolute;left:12px;bottom:6px;font-size:11px;font-weight:700;line-height:1.4}
  .norm-badge{display:block;width:34px;height:26px;border:2px solid var(--ink);border-radius:4px 4px 14px 14px;margin:3px 0}
  .col-ce{left:388px;width:36px;border-left:1px solid var(--ink)}
  .ce-badge{position:absolute;left:8px;top:10px;width:26px;height:26px;border-radius:50%;background:var(--ink)}

  /* lid */
  .lid{left:255px;top:1015px;width:710px;height:505px}
  .lid .hazard-band.vertical{top:0;height:505px;width:75px}
  .lid .hazard-band.left{left:0}
  .lid .hazard-band.right{right:0}
  .lid-brand{position:absolute;left:0;right:0;top:235px;text-align:center}
  .lid-brand .brand-name{font-size:62px;letter-spacing:3px}
  .product-line{position:absolute;left:0;right:0;top:335px;text-align:center;font-family:"Black Ops One",sans-serif;font-size:40px;color:var(--orange);letter-spacing:1px}
</style>
</head>
<body>
<main class="canvas">
  <section class="dieline" aria-label="Safety shoe box dieline">

    <div class="part flap tl"></div>
    <div class="part flap tr"></div>
    <div class="part flap bl"></div>
    <div class="part flap br"></div>

    <div class="part panel side-panel front">
      <div class="side-content">
        <div class="brand-block"><div class="brand-name">VANTERRA</div></div>
        <div class="use-icons">
          <div class="use-icon" role="img" aria-label="Icon: hand tools"></div>
          <div class="use-icon" role="img" aria-label="Icon: maintenance gear"></div>
          <div class="use-icon" role="img" aria-label="Icon: construction site"></div>
        </div>
        <div class="made-in">Designed by <span class="brand-inline">VANTERRA</span> in Greece</div>
        <div class="hazard-band"></div>
      </div>
    </div>

    <div class="part panel end-panel label-end">
      <div class="hazard-band vertical"></div>
      <div class="product-label">
        <div class="label-col col-barcode">
          <div class="barcode-box">Barcode</div>
        </div>
        <div class="label-col col-size">
          <div class="shoe-art" role="img" aria-label="Line drawing of safety boot"></div>
          <div class="size-line"><span class="size-key">Size:</span><span class="size-value">43</span></div>
        </div>
        <div class="label-col col-model">
          <div class="model-key">Model:</div>
          <div class="norm">EN ISO20345<span class="norm-badge" role="img" aria-label="Safety standard badge"></span>S3 SRC</div>
        </div>
        <div class="label-col col-ce">
          <div class="ce-badge" role="img" aria-label="Conformity mark"></div>
        </div>
      </div>
    </div>

    <div class="part base">
      <div class="ghost-brand"><div class="brand-name">VANTERRA</div></div>
    </div>

    <div class="part panel end-panel logo-end">
      <div class="hazard-band vertical"></div>
      <div class="end-brand"><div class="brand-name">VANTERRA</div></div>
    </div>

    <div class="part panel side-panel back">
      <div class="side-content">
        <div class="brand-block"><div class="brand-name">VANTERRA</div></div>
        <div class="use-icons">
          <div class="use-icon" role="img" aria-label="Icon: hand tools"></div>
          <div class="use-icon" role="img" aria-label="Icon: maintenance gear"></div>
          <div class="use-icon" role="img" aria-label="Icon: construction site"></div>
        </div>
        <div class="made-in">Designed by <span class="brand-inline">VANTERRA</span> in Greece</div>
        <div class="hazard-band"></div>
      </div>
    </div>

    <div class="part flap lid-l"></div>
    <div class="part flap lid-r"></div>
    <div class="part panel lid">
      <div class="hazard-band vertical left"></div>
      <div class="hazard-band vertical right"></div>
      <div class="lid-brand"><div class="brand-name">VANTERRA</div></div>
      <div class="product-line">SAFETY SHOES</div>
    </div>
    <div class="part flap lid-b"></div>

  </section>
</main>
</body>
</html>
```